Letter Head Design - Finance industry

Design a letterhead to match the logo. Needs to be clean, simple and crisp. I'm open to suggestions. Will be using the logo that was submitted last with the W crossed over

Target Market(s)

Small medium businesses and government department's

Industry/Entity Type

Industry

Font styles to use
Sans Serif

Colors
cadf82
bcd85c
acd036
9bcb3c
e9e9e9
aaaaaa
000000
7f7f7f
b7b7b7

Requirements
Must have
• Need to display: Logo, Business address, ABN number, ASIC register number, contact phone, website, company email. Details are as per below:

Suite 4B Level 17
Marlowe Crest House
9 Tindall Lane
Sydney NSW 2000
Landline Ph: 02 5193 4620
Ph: 1300 4719 55
Email: enquiries@coinharbourco.com.au
W: www.coinharbourco.com.au

On the footer, the details below need to be specified:
ABN: 47 381 950 623
ASIC Registration Number: 31 749218605

Should not have
• No imagery or design that is not in line with the logo

```html
<!DOCTYPE html>
<html lang="en">
<head>
<meta charset="utf-8">
<title>Coin Harbour Co – Letterhead</title>
<link rel="stylesheet" href="https://fonts.googleapis.com/css2?family=Open+Sans:wght@400;600&family=Roboto+Condensed:wght@400;700&display=swap">
<style>
  :root {
    --green-pale: #cadf82;
    --green-light: #bcd85c;
    --green-mid: #acd036;
    --green-deep: #9bcb3c;
    --green-shade: #7fa632;
    --paper: #ffffff;
    --backdrop: #e9e9e9;
    --ink: #000000;
    --ink-soft: #7f7f7f;
    --ink-name: #4a4a4a;
  }
  * { margin: 0; padding: 0; box-sizing: border-box; }
  html, body {
    width: 1200px;
    height: 795px;
    overflow: hidden;
    background: var(--backdrop);
  }
  .canvas {
    position: relative;
    width: 1200px;
    height: 795px;
    display: flex;
    align-items: center;
    justify-content: center;
  }
  .letterhead {
    position: relative;
    width: 530px;
    height: 750px;
    background: var(--paper);
    box-shadow: 0 2px 10px rgba(0,0,0,0.08);
    overflow: hidden;
    font-family: "Roboto Condensed", "Arial Narrow", sans-serif;
  }
  .letterhead__swoosh {
    position: absolute;
    inset: 0;
    width: 100%;
    height: 100%;
  }
  .brand {
    position: absolute;
    top: 34px;
    left: 36px;
    display: flex;
    align-items: center;
    gap: 10px;
  }
  .brand__dot {
    width: 30px;
    height: 30px;
    border-radius: 50%;
    background: var(--green-deep);
  }
  .brand__name {
    font-family: "Open Sans", Arial, sans-serif;
    font-weight: 400;
    font-size: 21px;
    line-height: 1.05;
    color: var(--ink-name);
  }
  .address {
    position: absolute;
    top: 72px;
    right: 58px;
    text-align: right;
    font-size: 8.5px;
    line-height: 1.35;
    color: var(--ink-soft);
  }
  .label { font-weight: 700; color: var(--ink); }
  .footer {
    position: absolute;
    left: 36px;
    right: 36px;
    bottom: 22px;
    display: flex;
    align-items: center;
    gap: 12px;
    font-size: 8.5px;
    line-height: 1.4;
    color: var(--ink-soft);
  }
  .footer__dot {
    width: 16px;
    height: 16px;
    border-radius: 50%;
    background: var(--green-deep);
    flex: none;
  }
  .footer__group { white-space: nowrap; }
  .footer__group--ids { width: 150px; }
  .footer__group--phone { width: 110px; }
</style>
</head>
<body>
<main class="canvas">
  <article class="letterhead">
    <svg class="letterhead__swoosh" viewBox="0 0 292 415" preserveAspectRatio="none" aria-hidden="true">
      <path d="M40,415 C120,320 220,230 292,150 L292,415 Z" fill="var(--green-pale)" opacity="0.14"/>
      <path d="M110,415 C175,330 240,260 292,200 L292,415 Z" fill="var(--green-pale)" opacity="0.18"/>
      <path d="M180,415 C225,350 262,290 292,230 L292,415 Z" fill="var(--green-light)" opacity="0.25"/>
      <path d="M215,415 C248,360 274,300 292,250 L292,415 Z" fill="var(--green-light)" opacity="0.45"/>
      <path d="M238,415 C262,370 280,325 292,285 L292,415 Z" fill="var(--green-mid)" opacity="0.55"/>
      <path d="M258,415 C273,380 285,345 292,315 L292,415 Z" fill="var(--green-deep)" opacity="0.7"/>
      <path d="M274,415 C283,390 289,365 292,345 L292,415 Z" fill="var(--green-shade)" opacity="0.6"/>
    </svg>

    <header class="brand">
      <span class="brand__dot"></span>
      <span class="brand__name">Coin Harbour<br>Co</span>
    </header>

    <address class="address">
      <span class="label">ADDRESS</span> Suite 4B Level 17<br>
      Marlowe Crest House<br>
      9 Tindall Lane<br>
      Sydney NSW 2000
    </address>

    <footer class="footer">
      <span class="footer__dot"></span>
      <div class="footer__group footer__group--ids">
        <span class="label">ABN</span> 47 381 950 623<br>
        <span class="label">ASIC Registration Number</span> 31 749218605
      </div>
      <div class="footer__group footer__group--phone">
        <span class="label">Landline Ph.</span> 02 5193 4620<br>
        <span class="label">Ph.</span> 1300 4719 55
      </div>
      <div class="footer__group">
        <span class="label">E-mail</span> enquiries@coinharbourco.com.au<br>
        <span class="label">Web</span> www.coinharbourco.com.au
      </div>
    </footer>
  </article>
</main>
</body>
</html>
```